Design a Website for an IT Support Company

We are an IT support company that provides commercial IT support and services to small and medium sized businesses. We are in need of a website to be developed for our business.
We would like to work with someone who is either familiar with the IT field, or has developed a website for an IT support company in the past.
Some examples of designs/layouts that we like:
https://www.velmorask.example/
http://www.quibenstack.example/
http://572zo.example/
http://www.guspelnetworks.example/
http://www.ourba.example/
I have attached a word document that gives a menu system/page layout format that we would like for our website as well as branch office phone numbers. Our logo is also attached that you can use for your design purposes. We currently do not have copy produced for all of the pages outlined in the word document, but would get this done during the project with the selected designer.
We would like the website to be SEO friendly & fully responsive. We would prefer a Wordpress format, however, we are open to HTML formats as well.

```html
<!DOCTYPE html>
<html lang="en">
<head>
<meta charset="utf-8">
<title>Brisklane IT – IT Support Company</title>
<link rel="stylesheet" href="https://fonts.googleapis.com/css2?family=Exo+2:ital,wght@0,400;0,500;0,600;0,700;1,700;1,800&family=Arimo:ital,wght@0,400;0,700;1,400&display=swap">
<style>
:root{
  --blue:#0a72c4;
  --blue-deep:#0461ad;
  --ink:#151515;
  --text:#555a60;
  --white:#ffffff;
  --footer:#232323;
  --footer-bottom:#141414;
  --footer-text:#d9d9d9;
  --rule:#3a3a3a;
}
*{margin:0;padding:0;box-sizing:border-box}
html,body{width:1200px;height:2605px;overflow:hidden}
body{position:relative;background:var(--white);font-family:"Arimo",Arial,sans-serif;color:var(--text)}
.abs{position:absolute}
.heading{font-family:"Exo 2",sans-serif}

/* hero */
.hero{left:0;top:0;width:1200px;height:680px;
  background:radial-gradient(circle at 900px 330px,#f6b24a 0,#c77a2e 10%,rgba(40,50,70,0) 30%),
  linear-gradient(180deg,#e9eef3 0%,#aebdcc 40%,#55708e 75%,#2a4466 100%)}
.hero-curve{left:0;top:560px;width:1200px;height:130px}
.topbar{right:0;top:0;width:560px;height:44px;background:#111;opacity:.9}
.top-social{top:12px;width:16px;height:16px;border-radius:50%;background:#cfd6de}
.top-mail{left:724px;top:9px;font-size:15px;color:var(--white)}
.top-phone{left:912px;top:0;width:210px;height:52px;background:var(--blue);color:var(--white);
  font-size:21px;display:flex;align-items:center;justify-content:center;gap:10px;border-radius:0 0 4px 4px}
.logo{display:flex;align-items:center;gap:10px;font-family:"Exo 2",sans-serif;font-weight:600}
.hero-logo{left:78px;top:80px;font-size:34px;color:#1d2630}
.logo-dot{width:22px;height:22px;border-radius:50%;background:var(--blue)}
.nav{left:388px;top:90px;display:flex;gap:40px;font-family:"Exo 2",sans-serif;font-weight:600;font-size:18px;color:#1d2630}
.hero-kicker{left:78px;top:242px;font-size:29px;font-weight:500;color:#111}
.hero-title{left:78px;top:278px;font-size:54px;font-weight:800;font-style:italic;color:var(--blue)}
.hero-sub{left:78px;top:352px;width:520px;font-size:21px;line-height:31px;color:#1e2a36}
.btn{background:var(--blue);color:var(--white);border-radius:26px;display:flex;align-items:center;justify-content:center;font-family:"Arimo",sans-serif;font-size:19px;text-transform:uppercase}
.hero-btn{left:78px;top:443px;width:177px;height:48px}

/* welcome */
.welcome-title{left:0;top:695px;width:1200px;display:flex;justify-content:center;align-items:center;gap:14px;font-size:46px;font-weight:600;color:var(--ink)}
.welcome-title .brand{color:var(--ink)}
.para{font-size:14px;line-height:25px;color:#666}
.welcome-text{left:168px;top:772px;width:870px;text-align:center}
.welcome-btn{left:516px;top:919px;width:167px;height:50px}

/* services */
.services-band{left:0;top:1000px;width:1200px;height:640px}
.what-title{left:0;top:1075px;width:1200px;text-align:center;font-size:46px;font-weight:600;color:var(--white)}
.svc-title{font-family:"Exo 2",sans-serif;font-size:29px;font-weight:600;color:var(--white)}
.svc-list{list-style:none;font-size:14.5px;line-height:25px;color:var(--white)}
.data-title{right:863px;top:1184px}
.data-list{right:863px;top:1226px;text-align:right}
.voice-title{left:863px;top:1194px}
.voice-list{left:863px;top:1236px}
.cloud-title{left:0;width:1200px;top:1390px;text-align:center}
.cloud-list{left:0;width:1200px;top:1432px;text-align:center}

/* why */
.why-title{left:78px;top:1648px;font-size:45px;font-weight:600;color:var(--ink)}
.why-text{left:78px;top:1715px;width:625px}
.why-btn{left:78px;top:1918px;width:165px;height:50px}
.why-screen{left:770px;top:1681px;width:352px;height:287px;border-radius:6px;
  background:linear-gradient(180deg,#2b2b2b 0,#2b2b2b 4%,#dfe6ee 4%,#c6d3e0 70%,#d8dadd 70%,#b9bcc0 100%)}
.why-shadow{left:420px;top:2016px;width:360px;height:18px;border-radius:50%;
  background:radial-gradient(ellipse at center,rgba(0,0,0,.2),rgba(0,0,0,0) 70%)}
.clients{left:78px;top:2078px;width:1044px;display:flex;justify-content:space-between;align-items:center}
.client{width:120px;height:44px;background:#d5dbe2;border-radius:4px}

/* footer */
.footer-wave{left:0;top:2120px;width:1200px;height:490px}
.footer-logo{left:99px;top:2325px;font-size:31px;color:var(--white)}
.social{top:2403px;width:40px;height:40px;border-radius:50%}
.foot-head{top:2260px;font-family:"Exo 2",sans-serif;font-size:19px;font-weight:600;color:var(--white);text-transform:uppercase}
.links{left:363px;top:2303px;list-style:none;font-size:14px;color:var(--footer-text)}
.links li{height:52px;display:flex;align-items:center;padding-left:22px}
.links li.active{width:167px;height:40px;border:1.5px solid var(--footer-text);border-radius:20px;margin-bottom:12px;color:var(--white)}
.slide-arrow{top:2261px;width:22px;height:22px;background:#5b5b5b;color:#ddd;font-size:12px;display:flex;align-items:center;justify-content:center}
.avatar{left:580px;top:2305px;width:62px;height:62px;border-radius:50%;background:linear-gradient(#c9ced4,#8e969f)}
.t-name{left:669px;top:2315px;font-size:17px;font-weight:700;color:var(--white)}
.t-role{left:669px;top:2338px;font-size:14px;font-style:italic;color:#a9a9a9}
.t-quote{left:584px;top:2380px;width:245px;font-size:13.5px;line-height:22px;font-style:italic;color:#a9a9a9}
.contacts{left:874px;top:2296px;list-style:none;font-size:15.5px;color:var(--white);width:246px}
.contacts li{height:42px;display:flex;align-items:center;gap:12px;border-bottom:1px solid var(--rule)}
.copyright{left:0;top:2545px;width:1200px;height:60px;background:var(--footer-bottom);color:#cfcfcf;font-size:15px;display:flex;align-items:center;justify-content:center}
.copyright .brand{color:var(--blue);margin:0 4px}
</style>
</head>
<body>

<header>
  <div class="abs hero" role="img" aria-label="Photo of a city skyline with a network of connected nodes and a hand holding a glowing wireless signal"></div>
  <svg class="abs hero-curve" viewBox="0 0 1200 130" preserveAspectRatio="none">
    <path d="M0 112 Q600 -30 1200 85 L1200 130 L0 130 Z" fill="#ffffff"/>
    <path d="M0 112 Q600 -30 1200 85" fill="none" stroke="#0a72c4" stroke-width="5"/>
  </svg>

  <div class="abs topbar"></div>
  <span class="abs top-social" style="left:565px"></span>
  <span class="abs top-social" style="left:597px"></span>
  <span class="abs top-social" style="left:631px"></span>
  <span class="abs top-social" style="left:665px"></span>
  <span class="abs top-mail">✉ info@brisklane.example</span>
  <a class="abs top-phone">
    <svg width="18" height="18" viewBox="0 0 24 24"><path fill="#fff" d="M6.6 10.8a15 15 0 0 0 6.6 6.6l2.2-2.2c.3-.3.7-.4 1-.2 1.1.4 2.3.6 3.6.6.6 0 1 .4 1 1V20c0 .6-.4 1-1 1A17 17 0 0 1 3 4c0-.6.4-1 1-1h3.5c.6 0 1 .4 1 1 0 1.3.2 2.5.6 3.6.1.3 0 .7-.2 1z"/></svg>
    555-014-7720
  </a>

  <div class="abs logo hero-logo"><span class="logo-dot"></span>Brisklane IT</div>
  <nav class="abs nav"><span>Home</span><span>Services</span><span>Why Brisklane IT</span><span>Contact</span></nav>

  <p class="abs heading hero-kicker">WE ARE AN</p>
  <h1 class="abs heading hero-title">IT Support Company</h1>
  <p class="abs hero-sub">that provides commercial IT support and services to small and medium sized businesses.</p>
  <a class="abs btn hero-btn">Call us now</a>
</header>

<section class="welcome">
  <h2 class="abs heading welcome-title">WELCOME TO <span class="brand">Brisklane IT</span></h2>
  <p class="abs para welcome-text">Lorem Ipsum is simply dummy text of the printing and typesetting industry. Lorem Ipsum has been the industry's standard dummy text ever since the 1500s, when an unknown printer took a galley of type and scrambled it to make a type specimen book. It has survived not only five centuries, but also the leap into electronic typesetting, remaining essentially unchanged. It was popularised in the 1960s with the release of Dryprint sheets containing Lorem Ipsum passages, and more recently with desktop publishing software like Folio Layout Writer including versions of Lorem Ipsum.</p>
  <a class="abs btn welcome-btn">Read more</a>
</section>

<section class="services">
  <svg class="abs services-band" viewBox="0 0 1200 640" preserveAspectRatio="none">
    <path d="M0 7 L1200 28 L1200 50 L0 34 Z" fill="#1a1a1a"/>
    <path d="M0 33 L1200 50 L1200 612 L0 607 Z" fill="#0a72c4"/>
    <path d="M0 607 L1200 612 L1200 630 Z" fill="#1a1a1a"/>
    <g fill="none" stroke="#ffffff" stroke-width="1.5">
      <path d="M460 1238 Q545 1238 568 1165" transform="translate(0,-1000)"/>
      <path d="M599 188 L599 282"/>
      <path d="M634 165 Q660 238 756 238"/>
    </g>
    <g fill="#ffffff">
      <circle cx="568" cy="165" r="5"/><circle cx="599" cy="188" r="5"/><circle cx="634" cy="165" r="5"/>
    </g>
    <g stroke="#ffffff" fill="#ffffff">
      <circle cx="408" cy="238" r="56" fill="none" stroke-width="2" opacity=".6"/>
      <circle cx="408" cy="238" r="48"/>
      <circle cx="808" cy="238" r="56" fill="none" stroke-width="2" opacity=".6"/>
      <circle cx="808" cy="238" r="48"/>
      <circle cx="599" cy="334" r="56" fill="none" stroke-width="2" opacity=".6"/>
      <circle cx="599" cy="334" r="48"/>
    </g>
    <g fill="none" stroke="#111" stroke-width="3">
      <ellipse cx="408" cy="221" rx="19" ry="6"/>
      <path d="M389 221 v34 a19 6 0 0 0 38 0 v-34 M389 233 a19 6 0 0 0 38 0 M389 244 a19 6 0 0 0 38 0"/>
      <path d="M580 346 h38 a11 11 0 0 0 0-22 a16 16 0 0 0-30-4 a11 11 0 0 0-8 26 z"/>
      <path d="M782 238 v0 M789 230 v16 M796 222 v32 M803 232 v12 M810 218 v40 M817 228 v20 M824 234 v8 M831 238 v0" stroke-linecap="round"/>
    </g>
  </svg>

  <h2 class="abs heading what-title">WHAT WE Do</h2>

  <h3 class="abs svc-title data-title">Data</h3>
  <ul class="abs svc-list data-list">
    <li>Managed IT Services</li><li>IT Support &amp; Consulting</li><li>IT Helpdesk Services</li>
    <li>Network Security</li><li>Data Backup &amp; Recovery</li><li>Servers &amp; Virtualization</li>
    <li>Remote Monitoring Services</li><li>Wireless Networking</li><li>Email &amp; Spam Threat Management</li>
    <li>Structured Cabling</li>
  </ul>

  <h3 class="abs svc-title voice-title">Voice</h3>
  <ul class="abs svc-list voice-list">
    <li>Open PBX Consulting</li><li>Business Telephone Systems</li><li>Multiple Office Phone Systems</li>
    <li>Tellwave Telephone Systems</li><li>SIP Trunks</li>
  </ul>

  <h3 class="abs svc-title cloud-title">Cloud</h3>
  <ul class="abs svc-list cloud-list">
    <li>Cloud Suite Migrations</li><li>Nimbra Cloud Management Services</li><li>Cloud Migration Services</li>
    <li>Hosted Virtual Servers</li><li>Hosted Telephone Systems</li>
  </ul>
</section>

<section class="why">
  <h2 class="abs heading why-title">WHY Brisklane IT</h2>
  <p class="abs para why-text">Lorem Ipsum is simply dummy text of the printing and typesetting industry. Lorem Ipsum has been the industry's standard dummy text ever since the 1500s, when an unknown printer took a galley of type and scrambled it to make a type specimen book. It has survived not only five centuries, but also the leap into electronic typesetting, remaining essentially unchanged. It was popularised in the 1960s with the release of Dryprint sheets containing Lorem Ipsum passages, and more recently with desktop publishing software like Folio Layout Writer including versions of Lorem Ipsum.</p>
  <a class="abs btn why-btn">Read more</a>
  <div class="abs why-screen" role="img" aria-label="Desktop monitor showing a support agent with a headset in an office"></div>
  <div class="abs why-shadow"></div>
  <div class="abs clients">
    <span class="client"></span><span class="client" style="width:60px;height:60px"></span><span class="client"></span>
    <span class="client" style="border-radius:50%;height:60px"></span><span class="client"></span><span class="client"></span>
  </div>
</section>

<footer>
  <svg class="abs footer-wave" viewBox="0 0 1200 490" preserveAspectRatio="none">
    <path d="M0 8 Q600 140 1200 8 L1200 490 L0 490 Z" fill="#0a72c4"/>
    <path d="M0 22 Q600 170 1200 22 L1200 490 L0 490 Z" fill="#ffffff"/>
    <path d="M0 34 Q600 170 1200 34 L1200 490 L0 490 Z" fill="#232323"/>
  </svg>

  <div class="abs logo footer-logo"><span class="logo-dot"></span>Brisklane IT</div>
  <span class="abs social" style="left:110px;background:#3b5a9a"></span>
  <span class="abs social" style="left:157px;background:#1da1f2"></span>
  <span class="abs social" style="left:204px;background:#d6412b"></span>
  <span class="abs social" style="left:253px;background:#0a72c4"></span>

  <h4 class="abs foot-head" style="left:365px">Useful Links</h4>
  <ul class="abs links">
    <li class="active">HOME</li><li>SERVICES</li><li>WHY BRISKLANE IT</li><li>CONTACT</li>
  </ul>

  <h4 class="abs foot-head" style="left:584px">Testimonials</h4>
  <span class="abs slide-arrow" style="left:787px">‹</span>
  <span class="abs slide-arrow" style="left:812px">›</span>
  <div class="abs avatar" role="img" aria-label="Portrait photo of the client"></div>
  <p class="abs t-name">Marten Olvik</p>
  <p class="abs t-role">CEO</p>
  <p class="abs t-quote">"Lorem Ipsum is simply dummy text of the printing and typesetting industry. Lorem Ipsum has been the industry's standard dummy text ever since the 1500s, when an unknown printer took a galley of type."</p>

  <h4 class="abs foot-head" style="left:874px">Contact Us</h4>
  <ul class="abs contacts">
    <li><svg width="14" height="14" viewBox="0 0 24 24"><path fill="#0a72c4" d="M6.6 10.8a15 15 0 0 0 6.6 6.6l2.2-2.2c.3-.3.7-.4 1-.2 1.1.4 2.3.6 3.6.6.6 0 1 .4 1 1V20c0 .6-.4 1-1 1A17 17 0 0 1 3 4c0-.6.4-1 1-1h3.5c.6 0 1 .4 1 1 0 1.3.2 2.5.6 3.6.1.3 0 .7-.2 1z"/></svg>Houston: 555-018-3301</li>
    <li><svg width="14" height="14" viewBox="0 0 24 24"><path fill="#0a72c4" d="M6.6 10.8a15 15 0 0 0 6.6 6.6l2.2-2.2c.3-.3.7-.4 1-.2 1.1.4 2.3.6 3.6.6.6 0 1 .4 1 1V20c0 .6-.4 1-1 1A17 17 0 0 1 3 4c0-.6.4-1 1-1h3.5c.6 0 1 .4 1 1 0 1.3.2 2.5.6 3.6.1.3 0 .7-.2 1z"/></svg>San Antonio: 555-016-4412</li>
    <li><svg width="14" height="14" viewBox="0 0 24 24"><path fill="#0a72c4" d="M6.6 10.8a15 15 0 0 0 6.6 6.6l2.2-2.2c.3-.3.7-.4 1-.2 1.1.4 2.3.6 3.6.6.6 0 1 .4 1 1V20c0 .6-.4 1-1 1A17 17 0 0 1 3 4c0-.6.4-1 1-1h3.5c.6 0 1 .4 1 1 0 1.3.2 2.5.6 3.6.1.3 0 .7-.2 1z"/></svg>Austin: 555-019-5523</li>
    <li><svg width="14" height="14" viewBox="0 0 24 24"><path fill="#0a72c4" d="M6.6 10.8a15 15 0 0 0 6.6 6.6l2.2-2.2c.3-.3.7-.4 1-.2 1.1.4 2.3.6 3.6.6.6 0 1 .4 1 1V20c0 .6-.4 1-1 1A17 17 0 0 1 3 4c0-.6.4-1 1-1h3.5c.6 0 1 .4 1 1 0 1.3.2 2.5.6 3.6.1.3 0 .7-.2 1z"/></svg>Tulsa: 555-013-6634</li>
    <li><svg width="14" height="14" viewBox="0 0 24 24"><path fill="#0a72c4" d="M6.6 10.8a15 15 0 0 0 6.6 6.6l2.2-2.2c.3-.3.7-.4 1-.2 1.1.4 2.3.6 3.6.6.6 0 1 .4 1 1V20c0 .6-.4 1-1 1A17 17 0 0 1 3 4c0-.6.4-1 1-1h3.5c.6 0 1 .4 1 1 0 1.3.2 2.5.6 3.6.1.3 0 .7-.2 1z"/></svg>Oklahoma City: 555-017-7745</li>
  </ul>

  <p class="abs copyright">© <span class="brand">Brisklane IT</span> - 2017. All Rights Reserved.</p>
</footer>

</body>
</html>
```